Highly motivated family winery needs new wine labels.

Company and target group:
We are a smaller, family-run winery in the heart of Germany and focus on quality rather than quantity. We primarily market to private customers, but are also represented in food retail. The wines appeal to both younger and older wine drinkers (30 – 80 years old). The labels should also be accordingly.
Requirements and wishes:
We would like to have a new logo consisting of the letters L and T that can be used in both 1 color and 2 colors. The family name “Tessendorf” should appear on the label, with the font being left to the creativity of the designers. The size of the label has not yet been fixed, but it should run around the bottle and therefore have a front and back (around 160mm wide and 80mm high). The design should be simple, modern and not too ornate.
The currently 22 types of wine/sparkling wine should all have the same label, but we would like to color-code the flavors in some way.
Perhaps the silhouette of one of the buildings of our winery (with the tower) can be incorporated into the design of the label (see picture).
A central element of the labels should have a high recognition value and be placed on the front of the label with the later wine type information.
We look forward to your suggestions.
Wegen der Weihnachtsfeiertage möchte ich das Projekt verlängern, um den Designern mehr Zeit zu geben. Bisher sind auch nur wenige Worschläge eingegangen.

```html
<!DOCTYPE html>
<html lang="en">
<head>
<meta charset="utf-8">
<title>Tessendorf Wine Label</title>
<link rel="stylesheet" href="https://fonts.googleapis.com/css2?family=Lato:wght@400&family=Playfair+Display:wght@700&family=Roboto+Condensed:wght@300&display=swap">
<style>
  :root {
    --canvas-bg: #ffffff;
    --label-grey: #5f605e;
    --label-paper: #f4f6f7;
    --gold-dark: #a8874f;
    --gold-light: #ecd08a;
    --illustration-grey: #767676;
    --band-grey: #6c6c6c;
    --text-light: #ffffff;
  }
  html, body {
    margin: 0;
    padding: 0;
    width: 1200px;
    height: 1200px;
    overflow: hidden;
    background: var(--canvas-bg);
  }
  .canvas {
    position: relative;
    width: 1200px;
    height: 1200px;
  }
  .wine-label {
    position: absolute;
    left: 390px;
    top: 202px;
    width: 420px;
    height: 795px;
  }
  .label-back { fill: var(--label-grey); }
  .label-paper { fill: var(--label-paper); }
  .label-frame { fill: none; stroke: url(#goldStroke); stroke-width: 5; }
  .tower-illustration { fill: var(--illustration-grey); }
  .gold-rule { fill: var(--gold-dark); }
  .monogram {
    font-family: "Playfair Display", serif;
    font-weight: 700;
    font-size: 180px;
    fill: var(--gold-dark);
  }
  .name-band { fill: var(--band-grey); }
  .brand-name {
    font-family: "Playfair Display", serif;
    font-weight: 700;
    font-size: 15px;
    letter-spacing: 0.5px;
    fill: var(--text-light);
  }
  .volume-line {
    font-family: "Roboto Condensed", sans-serif;
    font-weight: 300;
    font-size: 22px;
    fill: var(--text-light);
  }
  .volume-mark {
    font-family: "Lato", sans-serif;
    font-size: 38px;
    fill: var(--text-light);
  }
  .label-note {
    font-family: "Lato", sans-serif;
    font-size: 13px;
    fill: var(--text-light);
  }
</style>
</head>
<body>
<main class="canvas">
  <svg class="wine-label" viewBox="0 0 420 795" xmlns="http://www.w3.org/2000/svg">
    <defs>
      <linearGradient id="goldStroke" x1="0" y1="0" x2="1" y2="1">
        <stop offset="0" stop-color="#a8874f"/>
        <stop offset="0.35" stop-color="#ecd08a"/>
        <stop offset="0.7" stop-color="#a8874f"/>
        <stop offset="1" stop-color="#c9a963"/>
      </linearGradient>
      <clipPath id="frontArea">
        <path d="M5,190 C5,80 120,12 250,5 C360,0 420,70 418,190 C414,380 385,550 345,675 C230,670 100,620 50,520 C25,460 12,330 5,190 Z"/>
      </clipPath>
    </defs>

    <path class="label-back" d="M5,190 C5,80 120,12 250,5 C360,0 420,70 418,190 C415,400 390,620 345,790 C200,785 60,740 30,650 C15,520 8,350 5,190 Z"/>
    <path class="label-paper" d="M5,190 C5,80 120,12 250,5 C360,0 420,70 418,190 C414,380 385,550 345,675 C230,670 100,620 50,520 C25,460 12,330 5,190 Z"/>

    <g clip-path="url(#frontArea)">
      <rect class="tower-illustration" x="122" y="72" width="192" height="180" rx="6" role="img" aria-label="Illustration of the winery tower roof and upper storey"/>
      <rect class="tower-illustration" x="150" y="515" width="133" height="140" role="img" aria-label="Illustration of the winery tower base with doorway"/>
    </g>

    <path class="label-frame" d="M5,190 C5,80 120,12 250,5 C360,0 420,70 418,190 C414,380 385,550 345,675 C230,670 100,620 50,520 C25,460 12,330 5,190 Z"/>

    <rect class="gold-rule" x="150" y="252" width="133" height="4"/>

    <text class="monogram" x="216" y="455" text-anchor="middle">LT</text>

    <rect class="gold-rule" x="150" y="485" width="133" height="3"/>
    <rect class="name-band" x="150" y="488" width="133" height="27"/>
    <text class="brand-name" x="216" y="507" text-anchor="middle">Tessendorf</text>

    <text class="volume-line" x="75" y="682">750 ml <tspan class="volume-mark" dy="2">e</tspan><tspan dy="-2"> 18% vol</tspan></text>
    <text class="label-note" x="325" y="711" text-anchor="end">Lorem ipsum dolor sit amet, et assum</text>
    <text class="label-note" x="325" y="729" text-anchor="end">ignota temporibus vix.</text>
  </svg>
</main>
</body>
</html>
```